tillstop Fountain Drink Program header Design

Designing a fountain drink machine graphics that attract to customers to buy the fountain drink. Along with the attractive price point on it. I am attaching my current program graphics on the machine but want to create something more attractive. Also want to incorporate our brand logo with it. Pay Less 79c is my current Design. tillstop is my convenience store brand name. The design theme should consist of ice cold fountain drink and price point of 79c for 32 oz. the fountain drink cups we have are white foam cups with tillstop logo on them. see attached as well

Target Market(s)

Thirsty Consumers

Industry/Entity Type

Convenience Store

Colors
acd136
fbed22
33a6d7

Requirements
Must have
• Ice Cold Drink theme

```html
<!DOCTYPE html>
<html lang="en">
<head>
<meta charset="utf-8">
<title>tillstop Fountain Drink Header</title>
<link rel="stylesheet" href="https://fonts.googleapis.com/css2?family=Open+Sans:wght@700;800&display=swap">
<style>
  :root {
    --sky-light: #8ee6fb;
    --sky-mid: #46c4ee;
    --sky-deep: #2aa3d8;
    --lime: #9fd330;
    --accent-green: #8cc63e;
    --ink: #161616;
    --white: #f4fbf4;
    --ice: #5ab6e8;
    --ice-deep: #2f86cf;
  }
  * { margin: 0; padding: 0; box-sizing: border-box; }
  html, body { width: 1200px; height: 425px; overflow: hidden; background: #ffffff; }
  .banner {
    position: relative;
    width: 1200px;
    height: 425px;
    overflow: hidden;
    font-family: "Open Sans", Arial, sans-serif;
    background: linear-gradient(100deg, var(--sky-mid) 0%, var(--sky-light) 45%, var(--sky-mid) 75%, var(--sky-deep) 100%);
  }
  .banner__wave { position: absolute; inset: 0; width: 1200px; height: 425px; }
  .headline {
    position: absolute;
    left: 30px;
    top: 18px;
    font-size: 112px;
    font-weight: 800;
    line-height: 1;
    letter-spacing: -3px;
    color: var(--white);
    -webkit-text-stroke: 11px var(--ink);
    paint-order: stroke fill;
    white-space: nowrap;
  }
  .headline .accent { color: var(--accent-green); }
  .price {
    position: absolute;
    left: 40px;
    top: 179px;
    display: flex;
    align-items: flex-start;
  }
  .price__amount {
    font-size: 230px;
    font-weight: 800;
    line-height: 1;
    letter-spacing: -8px;
    color: var(--white);
    -webkit-text-stroke: 11px var(--ink);
    paint-order: stroke fill;
  }
  .price__side {
    display: flex;
    flex-direction: column;
    margin-left: 18px;
  }
  .price__cents {
    font-size: 88px;
    font-weight: 800;
    line-height: 1;
    color: var(--white);
    -webkit-text-stroke: 8px var(--ink);
    paint-order: stroke fill;
    margin-top: 6px;
  }
  .price__detail {
    margin-top: 26px;
    color: var(--white);
    font-weight: 700;
    font-size: 38px;
    line-height: 1.2;
    white-space: nowrap;
  }
  .cup-art {
    position: absolute;
    left: 880px;
    top: 104px;
    width: 248px;
    height: 298px;
  }
  .cup-art__fill {
    position: absolute;
    inset: 0;
    border-radius: 18px;
    background: radial-gradient(ellipse at 50% 45%, #f3f7f9 0%, #d9ecf5 45%, var(--ice) 80%, var(--ice-deep) 100%);
  }
  .cup-art__brand {
    position: absolute;
    left: 124px;
    top: 150px;
    transform: translate(-50%, -50%) rotate(-90deg);
    font-size: 46px;
    font-weight: 800;
    color: var(--ink);
    letter-spacing: -1px;
    white-space: nowrap;
  }
</style>
</head>
<body>
  <main class="banner">
    <svg class="banner__wave" viewBox="0 0 1200 425" aria-hidden="true">
      <defs>
        <linearGradient id="limeBand" x1="0" y1="0" x2="1" y2="1">
          <stop offset="0" stop-color="#b5e03a"/>
          <stop offset="0.6" stop-color="#9fd330"/>
          <stop offset="1" stop-color="#8cc92b"/>
        </linearGradient>
      </defs>
      <path d="M0 98 C 300 220, 650 360, 940 425 L 0 425 Z" fill="url(#limeBand)"/>
      <path d="M940 425 C 1040 405, 1130 385, 1200 376 L 1200 425 Z" fill="#2a9fd6" opacity="0.35"/>
    </svg>

    <h1 class="headline">P<span class="accent">a</span>y Less<span class="accent">!</span></h1>

    <div class="price">
      <div class="price__amount" aria-label="79 cents">79</div>
      <div class="price__side">
        <span class="price__cents" aria-hidden="true">¢</span>
        <p class="price__detail">32 oz<br>Fountain</p>
      </div>
    </div>

    <div class="cup-art">
      <div class="cup-art__fill" role="img" aria-label="White foam fountain cup filled with iced cola, surrounded by ice cubes and a cold water splash"></div>
      <span class="cup-art__brand">tillstop</span>
    </div>
  </main>
</body>
</html>
```